Tolvek Consulting
Tolvek Consulting stationary
Tolvek Consulting - Consulting
Creative Brief
Professional
Daniel R. Tolvek
Chief Executive Officer
Tolvek Consulting, LLC P.O. Box 4372 Phoenix, AZ 85004
daniel@danielrtolvek-mail.com
danielrtolvek-mail.com
Tolvek Consulting Logo

```html
<!DOCTYPE html>
<html lang="en">
<head>
<meta charset="utf-8">
<title>Tolvek Consulting — Stationery</title>
<link rel="stylesheet" href="https://fonts.googleapis.com/css2?family=Arimo:wght@400;700&display=swap">
<style>
  :root {
    --backdrop: #e6e4e1;
    --paper: #ffffff;
    --card-dark: #2a2b2e;
    --card-dark-edge: #1b1c1e;
    --brand-blue: #1f3f7a;
    --brand-orange: #f08a1c;
    --ink: #333333;
    --ink-soft: #6b6b6b;
    --ink-light: #c9ccd1;
    --shadow: rgba(0, 0, 0, 0.18);
  }
  * { box-sizing: border-box; margin: 0; padding: 0; }
  html, body { width: 1200px; height: 770px; overflow: hidden; }
  body {
    position: relative;
    background: var(--backdrop);
    font-family: "Arimo", Arial, sans-serif;
    color: var(--ink);
  }
  .sheet {
    position: absolute;
    background: var(--paper);
    box-shadow: 0 3px 10px var(--shadow);
  }
  .brand {
    display: flex;
    align-items: center;
    gap: 8px;
    font-weight: 700;
    color: var(--brand-blue);
    white-space: nowrap;
    letter-spacing: 0.01em;
  }
  .brand-mark {
    background: var(--brand-orange);
    flex: none;
  }

  /* Letterhead */
  .letterhead { left: 631px; top: 29px; width: 557px; height: 710px; }
  .letterhead .brand { position: absolute; left: 34px; top: 42px; font-size: 30px; gap: 12px; }
  .letterhead .brand-mark { width: 26px; height: 26px; }
  .letterhead-footer {
    position: absolute; left: 34px; bottom: 30px;
    font-size: 11.5px; line-height: 1.45; color: var(--ink);
  }

  /* Envelope */
  .envelope { left: 43px; top: 449px; width: 571px; height: 298px; }
  .envelope .brand { position: absolute; left: 26px; top: 40px; font-size: 24px; gap: 10px; }
  .envelope .brand-mark { width: 22px; height: 22px; }
  .envelope-return {
    position: absolute; left: 30px; bottom: 26px;
    font-size: 9.5px; color: var(--ink);
  }

  /* Business cards */
  .card {
    position: absolute; width: 216px; height: 122px;
    border-radius: 6px; overflow: hidden;
  }
  .card-light { background: linear-gradient(160deg, #ffffff 0%, #eef0f2 100%); }
  .card-dark { background: linear-gradient(160deg, var(--card-dark) 0%, var(--card-dark-edge) 100%); }
  .card-dark .brand { color: var(--ink-light); }
  .card .brand { position: absolute; font-size: 17px; gap: 7px; }
  .card .brand-mark { width: 15px; height: 15px; }
  .card-back .brand { left: 50%; top: 50%; transform: translate(-50%, -50%); }
  .card-front .brand { right: 14px; top: 16px; font-size: 14px; }
  .card-front .brand-mark { width: 12px; height: 12px; }
  .card-contact {
    position: absolute; left: 14px; top: 44px;
    font-size: 6.5px; line-height: 1.4; color: var(--ink);
  }
  .card-dark .card-contact { color: var(--ink-light); }
  .card-contact .person-name { font-weight: 700; font-size: 7.5px; }
  .card-contact .person-role { margin-bottom: 8px; color: var(--ink-soft); }
  .card-dark .card-contact .person-role { color: #9a9ca1; }

  .card-front-light { left: 43px; top: 58px; }
  .card-front-dark  { left: 276px; top: 58px; }
  .card-back-light  { left: 43px; top: 252px; }
  .card-back-dark   { left: 276px; top: 252px; }
</style>
</head>
<body>

  <section class="card card-light card-front card-front-light">
    <div class="brand"><span class="brand-mark"></span>Tolvek Consulting</div>
    <div class="card-contact">
      <div class="person-name">Daniel R. Tolvek</div>
      <div class="person-role">Chief Executive Officer</div>
      <div>Tolvek Consulting, LLC P.O. Box 4372 Phoenix, AZ 85004</div>
      <div>Cell: 480.555.0172</div>
      <div>Email: daniel@danielrtolvek-mail.com</div>
      <div>Web: danielrtolvek-mail.com</div>
    </div>
  </section>

  <section class="card card-dark card-front card-front-dark">
    <div class="brand"><span class="brand-mark"></span>Tolvek Consulting</div>
    <div class="card-contact">
      <div class="person-name">Daniel R. Tolvek</div>
      <div class="person-role">Chief Executive Officer</div>
      <div>Tolvek Consulting, LLC P.O. Box 4372 Phoenix, AZ 85004</div>
      <div>Cell: 480.555.0172</div>
      <div>Email: daniel@danielrtolvek-mail.com</div>
      <div>Web: danielrtolvek-mail.com</div>
    </div>
  </section>

  <section class="card card-light card-back card-back-light">
    <div class="brand"><span class="brand-mark"></span>Tolvek Consulting</div>
  </section>

  <section class="card card-dark card-back card-back-dark">
    <div class="brand"><span class="brand-mark"></span>Tolvek Consulting</div>
  </section>

  <section class="sheet envelope">
    <div class="brand"><span class="brand-mark"></span>Tolvek Consulting</div>
    <p class="envelope-return">Tolvek Consulting, LLC P.O. Box 4372 Phoenix, AZ 85004</p>
  </section>

  <section class="sheet letterhead">
    <div class="brand"><span class="brand-mark"></span>Tolvek Consulting</div>
    <footer class="letterhead-footer">
      <div>Tolvek Consulting, LLC, P.O. Box 4372, Phoenix, AZ 85004</div>
      <div>Cell : 480.555.0172 &nbsp;|&nbsp; Email : daniel@danielrtolvek-mail.com &nbsp;|&nbsp; Web : danielrtolvek-mail.com</div>
    </footer>
  </section>

</body>
</html>
```